Need Bold, Hip Card for Concert Ticket Website Gleaming Passes!

Hi there! I am putting together a business/website that sells event tickets (mostly concerts, but also some sports and theater). Think SeatNook, but much smaller. The site is called Gleaming Passes. I have a new logo (attached, with black/red/white color scheme), and am looking for a modern/cool/original business card design. Note that I am thinking of having the card itself in the shape of a ticket (die cut), so you may want to keep that in mind when designing, but I'm not set on that. I'm also open to alternative card sizes, thicknesses, glossy, spot UV, etc. in order to stand out. I'm attaching a potential die cut template and a sample card using that template in case you want to work with that.
Target Market(s)
Music fans, people that like going to see live events
Industry/Entity Type
Entertainment
Contact Information for Business Card
Information that I'd like to have:
website address - www.gleamingpasses.example
phone number: 1-833-5GLEAMNG (532-6264)
my name - Wendel Pike

```html
<!DOCTYPE html>
<html lang="en">
<head>
<meta charset="utf-8">
<title>Gleaming Passes – Business Card</title>
<link rel="stylesheet" href="https://fonts.googleapis.com/css2?family=Montserrat:wght@500;800&family=Oswald:wght@400;500&display=swap">
<style>
  :root {
    --stage: #6b6b6b;
    --ticket-red: #8a1c1e;
    --ink-black: #111111;
    --paper-white: #ffffff;
    --brand-red: #8e1b1b;
    --rule-grey: #2a2a2a;
    --band-text: #bdbdbd;
  }
  * { margin: 0; padding: 0; box-sizing: border-box; }
  html, body { width: 1200px; height: 766px; overflow: hidden; }
  body { background: var(--stage); position: relative; font-family: "Montserrat", sans-serif; }

  .ticket { position: absolute; width: 560px; height: 340px; }
  .ticket-shape { position: absolute; inset: 0; width: 560px; height: 340px; }

  .card-front { left: 50px; top: 80px; }
  .card-back { left: 590px; top: 346px; }

  .front-url {
    position: absolute; top: 0; left: 0; width: 560px; height: 50px;
    display: flex; align-items: center; justify-content: center;
    font-family: "Oswald", sans-serif; font-weight: 500; font-size: 16px;
    letter-spacing: 4px; color: var(--band-text); text-transform: uppercase;
  }
  .front-brand {
    position: absolute; top: 50px; left: 0; width: 560px; height: 240px;
    display: flex; align-items: center; justify-content: center; gap: 18px;
  }
  .brand-square { width: 58px; height: 58px; background: var(--paper-white); }
  .brand-name {
    font-family: "Montserrat", sans-serif; font-weight: 800; font-size: 44px;
    line-height: 1; color: var(--paper-white); text-transform: uppercase; letter-spacing: 2px;
  }

  .stub-brand {
    position: absolute; left: 60px; top: 170px;
    transform: translate(-50%, -50%) rotate(-90deg);
    display: flex; align-items: center; gap: 10px; white-space: nowrap;
  }
  .side-brand {
    position: absolute; left: 520px; top: 150px;
    transform: translate(-50%, -50%) rotate(90deg);
    display: flex; align-items: center; gap: 8px; white-space: nowrap;
  }
  .mini-square { width: 22px; height: 22px; background: var(--brand-red); }
  .mini-name {
    font-family: "Montserrat", sans-serif; font-weight: 800; font-size: 22px;
    color: var(--brand-red); text-transform: uppercase; letter-spacing: 1px;
  }
  .side-brand .mini-name { font-size: 17px; }
  .side-brand .mini-square { width: 18px; height: 18px; }

  .contact { position: absolute; left: 150px; top: 34px; width: 330px; }
  .holder-name {
    font-family: "Montserrat", sans-serif; font-weight: 500; font-size: 38px;
    color: var(--ink-black); text-transform: uppercase; letter-spacing: 1px;
    padding: 0 0 12px 12px; border-bottom: 2px solid var(--rule-grey);
  }
  .contact-line {
    font-family: "Oswald", sans-serif; font-size: 24px; padding: 14px 0 10px 0;
    border-bottom: 2px solid var(--rule-grey);
  }
  .phone { color: var(--ink-black); font-weight: 400; }
  .web { color: var(--brand-red); font-weight: 500; font-size: 20px; letter-spacing: 3px; text-transform: uppercase; }
</style>
</head>
<body>

  <section class="ticket card-front" aria-label="Card front">
    <svg class="ticket-shape" viewBox="0 0 560 340" aria-hidden="true">
      <defs>
        <clipPath id="ticket-outline-front">
          <path d="M28,0 H532 A28,28 0 0 0 560,28 V312 A28,28 0 0 0 532,340 H28 A28,28 0 0 0 0,312 V28 A28,28 0 0 0 28,0 Z"/>
        </clipPath>
      </defs>
      <g clip-path="url(#ticket-outline-front)">
        <rect width="560" height="340" fill="var(--ticket-red)"/>
        <rect width="560" height="50" fill="var(--ink-black)"/>
        <rect y="290" width="560" height="50" fill="var(--ink-black)"/>
      </g>
    </svg>
    <p class="front-url">www.gleamingpasses.example</p>
    <div class="front-brand">
      <span class="brand-square"></span>
      <span class="brand-name">Gleaming<br>Passes</span>
    </div>
  </section>

  <section class="ticket card-back" aria-label="Card back">
    <svg class="ticket-shape" viewBox="0 0 560 340" aria-hidden="true">
      <path d="M28,0 H532 A28,28 0 0 0 560,28 V312 A28,28 0 0 0 532,340 H28 A28,28 0 0 0 0,312 V28 A28,28 0 0 0 28,0 Z" fill="var(--paper-white)"/>
      <line x1="120" y1="0" x2="120" y2="340" stroke="var(--ink-black)" stroke-width="2" stroke-dasharray="10 8"/>
    </svg>
    <div class="stub-brand">
      <span class="mini-square"></span>
      <span class="mini-name">Gleaming Passes</span>
    </div>
    <div class="contact">
      <p class="holder-name">Wendel Pike</p>
      <p class="contact-line phone">1-833-5GLEAMNG (532-6264)</p>
      <p class="contact-line web">www.gleamingpasses.example</p>
    </div>
    <div class="side-brand">
      <span class="mini-square"></span>
      <span class="mini-name">Gleaming Passes</span>
    </div>
  </section>

</body>
</html>
```